LWT Company Overview and Framework Training Guide

I am creating a training guide that in intended to provide sales training to independent consultants. I am working on a new Company logo and would like to match the theme, but more importantly, I want to layout the content in a modern format that keeps users engaged. The sample logo is attached and I will add more blue before it's complete.

Target Market(s)

Technology sales reps and consultants

Industry/Entity Type

Information Technology

Font styles to use
Serif
Sans Serif

Colors
3176b5
0292cd
33a6d7
0355a3
ffffff
333333
606060
1b1b1b

Requirements
Must have
• I need a company overview and a few slides that define the problem my training will help solve. I also need to show the framework and sales process, along with a demo of the software platform.
Nice to have
• Video inserts would be helpful and some slide should allow me to build out steps of the workflow.

```html
<!DOCTYPE html>
<html lang="en">
<head>
<meta charset="utf-8">
<title>LWT Consulting Framework – Slides 7 to 11</title>
<link rel="stylesheet" href="https://fonts.googleapis.com/css2?family=Source+Sans+3:wght@400;600;700&display=swap">
<style>
  :root {
    --slide-blue: #0a55a3;
    --deep-blue: #0355a3;
    --mid-blue: #3176b5;
    --bright-blue: #0292cd;
    --sky-blue: #33a6d7;
    --pale-title: #d6effa;
    --white: #ffffff;
    --charcoal: #383838;
    --ink: #1b1b1b;
    --purple: #7030a0;
    --amber: #fbbc05;
    --circle-blue: #1a6fc4;
    --dot-green: #7ed957;
    --dot-teal: #2ad0c8;
  }
  * { box-sizing: border-box; margin: 0; padding: 0; }
  html, body { width: 1200px; height: 1079px; overflow: hidden; background: var(--white); }
  body { position: relative; font-family: "Source Sans 3", "Segoe UI", sans-serif; color: var(--white); }

  .slide {
    position: absolute; width: 550px; height: 309px; overflow: hidden;
    background: var(--slide-blue);
    box-shadow: 0 1px 4px rgba(0,0,0,0.25);
  }
  .slide--research { left: 39px; top: 38px; }
  .slide--proposal { left: 611px; top: 38px; }
  .slide--fulfillment { left: 39px; top: 385px; }
  .slide--engagement { left: 611px; top: 385px; }
  .slide--closing { left: 39px; top: 733px; background: var(--white); }

  .slide-number {
    position: absolute; left: 5px; top: 4px; width: 26px; height: 26px; border-radius: 50%;
    display: flex; align-items: center; justify-content: center;
    font-size: 9px; font-weight: 600;
  }
  .slide-number--light { background: var(--white); color: var(--ink); }
  .slide-number--dark { background: var(--deep-blue); color: var(--white); }

  .slide-title { position: absolute; font-size: 19px; font-weight: 400; white-space: nowrap; }
  .title-dots { position: absolute; display: flex; gap: 2px; }
  .title-dots span { width: 3px; height: 3px; border-radius: 50%; }
  .title-dots span:nth-child(1) { background: var(--bright-blue); }
  .title-dots span:nth-child(2) { background: var(--sky-blue); }
  .title-dots span:nth-child(3) { background: var(--dot-teal); }
  .title-dots span:nth-child(4) { background: var(--dot-green); }

  .framework-label {
    position: absolute; writing-mode: vertical-rl; transform: rotate(180deg);
    font-size: 6px; letter-spacing: 2.4px; color: rgba(255,255,255,0.85);
  }
  .site-footer { position: absolute; font-size: 5.5px; color: var(--white); }

  .bullet-list { position: absolute; list-style: none; }
  .bullet-list li { position: relative; padding-left: 13px; white-space: nowrap; }
  .bullet-list li::before {
    content: ""; position: absolute; left: 0; top: 50%; width: 3px; height: 3px;
    margin-top: -1.5px; border-radius: 50%; background: var(--white);
  }

  /* Slide 7 */
  .slide--research .slide-title { left: 0; width: 550px; text-align: center; top: 9px; }
  .slide--research .title-dots { left: 260px; top: 42px; }
  .research-list { left: 50px; top: 81px; font-size: 8.5px; }
  .research-list li { height: 27.5px; }
  .research-photo {
    position: absolute; left: 269px; top: 77px; width: 247px; height: 232px;
    background: linear-gradient(135deg, #e9eef7 0%, #b9c6dc 55%, #8f9fbb 100%);
  }
  .slide--research .framework-label { left: 10px; top: 130px; }
  .slide--research .site-footer { left: 6px; top: 298px; }

  /* Slide 8 */
  .proposal-photo {
    position: absolute; inset: 0;
    background: linear-gradient(120deg, #2a5f9e 0%, #1f5aa0 40%, #3d6eab 70%, #2c63a3 100%);
  }
  .slide--proposal .slide-title { left: 0; width: 570px; text-align: center; top: 11px; }
  .slide--proposal .title-dots { left: 266px; top: 41px; }
  .proposal-list { font-size: 9.5px; top: 65px; }
  .proposal-list li { height: 24.7px; }
  .proposal-list--primary { left: 141px; }
  .proposal-list--secondary { left: 292px; }
  .slide--proposal .framework-label { left: 10px; top: 130px; }
  .slide--proposal .site-footer { left: 6px; top: 298px; }

  /* Slide 9 */
  .dart-photo { position: absolute; left: 0; top: 0; }
  .slide--fulfillment .slide-title { right: 40px; top: 8px; }
  .slide--fulfillment .title-dots { left: 477px; top: 37px; }
  .fulfillment-list { position: absolute; right: 35px; top: 65px; list-style: none; text-align: right; font-size: 8.5px; }
  .fulfillment-list li { height: 27.5px; white-space: nowrap; }
  .slide--fulfillment .framework-label { left: 535px; top: 125px; }
  .slide--fulfillment .site-footer { right: 7px; top: 293px; }

  /* Slide 10 */
  .slide--engagement .slide-title {
    left: 0; width: 550px; text-align: center; top: 25px; font-size: 28px; color: var(--pale-title);
  }
  .slide--engagement .slide-title strong { font-weight: 700; }
  .play-mark { position: absolute; left: 0; top: 0; }
  .quote-mark { position: absolute; font-size: 46px; font-weight: 700; font-style: italic; line-height: 1; }
  .quote-mark--open { left: 268px; top: 123px; }
  .quote-mark--close { left: 496px; top: 214px; }
  .engagement-list { left: 321px; top: 139px; font-size: 10.5px; }
  .engagement-list li { height: 20.6px; }
  .slide--engagement .framework-label { left: 10px; top: 128px; }
  .slide--engagement .site-footer { left: 6px; top: 298px; }

  /* Slide 11 */
  .bubble { position: absolute; border-radius: 50%; }
  .bubble--main {
    left: 200px; top: 76px; width: 154px; height: 154px; background: var(--circle-blue);
    display: flex; align-items: center; justify-content: center; font-size: 23px; color: var(--white);
  }
  .bubble--dark { left: 379px; top: 12px; width: 102px; height: 102px; background: var(--charcoal); }
  .bubble--purple { left: 363px; top: 186px; width: 58px; height: 58px; background: var(--purple); }
  .bubble--amber { left: 137px; top: 203px; width: 44px; height: 44px; background: var(--amber); }
</style>
</head>
<body>

<section class="slide slide--research">
  <div class="slide-number slide-number--light">7</div>
  <h2 class="slide-title">Research &amp; Analysis</h2>
  <div class="title-dots"><span></span><span></span><span></span><span></span></div>
  <ul class="bullet-list research-list">
    <li>Provider Matrix &amp; Scoring</li>
    <li>Channel reviews &amp; rankings</li>
    <li>Short Lists – Evaluation Results</li>
    <li>Technical scopes &amp; POC</li>
    <li>Roadmap/Timeline</li>
    <li>Financial Analysis</li>
  </ul>
  <div class="research-photo" role="img" aria-label="Close-up photo of a keyboard key labelled Research"></div>
  <div class="framework-label">LWT Consulting Framework</div>
  <div class="site-footer">www.yoursite.com</div>
</section>

<section class="slide slide--proposal">
  <div class="proposal-photo" role="img" aria-label="Faded photo of a laptop showing analytics dashboards"></div>
  <div class="slide-number slide-number--dark">8</div>
  <h2 class="slide-title">Proposal Generation</h2>
  <div class="title-dots"><span></span><span></span><span></span><span></span></div>
  <ul class="bullet-list proposal-list proposal-list--primary">
    <li>Proper templates to use</li>
    <li>Executive Summary</li>
    <li>Challenges/Pain</li>
    <li>Potential Solutions</li>
    <li>Service Provider</li>
    <li>Marketplace</li>
    <li>Evaluation Data</li>
    <li>Financial Analysis</li>
    <li>Recommendation</li>
  </ul>
  <ul class="bullet-list proposal-list proposal-list--secondary">
    <li>TCO Analysis</li>
    <li>Intelligent Matrix (Weighted)</li>
    <li>Technical Diagrams</li>
    <li>Implementation Plans</li>
    <li>Timeline</li>
    <li>Expectations</li>
    <li>Cost/Benefit Analysis</li>
  </ul>
  <div class="framework-label">LWT Consulting Framework</div>
  <div class="site-footer">www.yoursite.com</div>
</section>

<section class="slide slide--fulfillment">
  <svg class="dart-photo" width="550" height="309" viewBox="0 0 550 309" role="img" aria-label="Photo of a dart hitting near the bullseye of a dartboard">
    <defs>
      <linearGradient id="dartTone" x1="0" y1="0" x2="1" y2="1">
        <stop offset="0" stop-color="#2b3a4a"/>
        <stop offset="0.45" stop-color="#8a6f55"/>
        <stop offset="1" stop-color="#1d2630"/>
      </linearGradient>
    </defs>
    <polygon points="0,0 139,0 375,309 0,309" fill="url(#dartTone)"/>
  </svg>
  <div class="slide-number slide-number--dark">9</div>
  <h2 class="slide-title">Fulfillment</h2>
  <div class="title-dots"><span></span><span></span><span></span><span></span></div>
  <ul class="fulfillment-list">
    <li>Presenting the solution</li>
    <li>Alignment with Success Criteria</li>
    <li>Customer Feedback and Direction</li>
    <li>Timelines &amp; Expectations</li>
    <li>Decision making process and support</li>
  </ul>
  <div class="framework-label">LWT Consulting Framework</div>
  <div class="site-footer">www.yoursite.com</div>
</section>

<section class="slide slide--engagement">
  <div class="slide-number slide-number--light">10</div>
  <h2 class="slide-title">On Going <strong>Engagement</strong></h2>
  <svg class="play-mark" width="550" height="309" viewBox="0 0 550 309" aria-hidden="true">
    <polygon points="113,98 201,179 113,259" fill="#ffffff"/>
  </svg>
  <span class="quote-mark quote-mark--open">“</span>
  <ul class="bullet-list engagement-list">
    <li>Managed TEM services</li>
    <li>Audits &amp; Cost containment</li>
    <li>Insights for future needs</li>
    <li>MACD work (UCaaS, Other)</li>
  </ul>
  <span class="quote-mark quote-mark--close">”</span>
  <div class="framework-label">LWT Consulting Framework</div>
  <div class="site-footer">www.yoursite.com</div>
</section>

<section class="slide slide--closing">
  <div class="bubble bubble--dark"></div>
  <div class="bubble bubble--main">Thank You!</div>
  <div class="bubble bubble--purple"></div>
  <div class="bubble bubble--amber"></div>
</section>

</body>
</html>
```